Well Designed, Impactful Business Card

I need a new business card designed that incorporates our company colors, looks very well designed, and is of the highest quality as that reflects the work we do as a professional services firm.

We would like it to incorporate a QR code and will link to an article we have written as a hook for potential clients. Designs should use the colors uploaded and can incorporate other colors to supplement the ones attached. The design should communicate professionalism, design, quality, and competence. Tagline can be used, but not required. Alternatively, a new one created. Current tagline is "Clearer Thinking, Bolder Results"

I would like for the two sides to be contrasting. If the front is colored, the back should be white (or light vs dark colors).

Old company website is here www.quillmorrow.net

```html
<!DOCTYPE html>
<html lang="en">
<head>
<meta charset="utf-8">
<title>Quill Morrow – Business Card</title>
<link href="https://fonts.googleapis.com/css2?family=Libre+Baskerville:wght@400;700&family=Poppins:wght@300;400&display=swap" rel="stylesheet">
<style>
  :root {
    --backdrop: #959595;
    --brand-orange: #f19b35;
    --card-white: #fdfdfd;
    --ink-dark: #3f3b38;
    --ink-light: #ffffff;
    --card-shadow: 0 18px 40px rgba(0,0,0,0.28);
  }
  * { box-sizing: border-box; margin: 0; padding: 0; }
  html, body {
    width: 1200px;
    height: 1050px;
    overflow: hidden;
    background: var(--backdrop);
  }
  .canvas {
    position: relative;
    width: 1200px;
    height: 1050px;
  }
  .card {
    position: absolute;
    left: 250px;
    width: 700px;
    height: 400px;
    box-shadow: var(--card-shadow);
  }
  /* Front side */
  .card--front {
    top: 85px;
    background: var(--brand-orange);
    color: var(--ink-light);
  }
  .card__frame {
    position: absolute;
    inset: 34px;
    border: 1.5px solid var(--ink-light);
  }
  .contact-block {
    position: absolute;
    left: 0;
    right: 0;
    top: 168px;
    display: flex;
    justify-content: center;
    align-items: center;
    gap: 22px;
  }
  .person { text-align: right; }
  .person__name {
    font-family: "Libre Baskerville", Georgia, serif;
    font-weight: 700;
    font-size: 27px;
    letter-spacing: -0.3px;
    line-height: 1.1;
  }
  .person__title {
    font-family: "Poppins", Arial, sans-serif;
    font-weight: 300;
    font-size: 16px;
    letter-spacing: 0.6px;
    margin-top: 2px;
  }
  .divider {
    width: 1.5px;
    height: 64px;
    background: var(--ink-light);
  }
  .details {
    list-style: none;
    font-family: "Poppins", Arial, sans-serif;
    font-weight: 300;
    font-size: 15px;
    letter-spacing: 0.5px;
    line-height: 1.35;
  }
  /* Back side */
  .card--back {
    top: 565px;
    background: var(--card-white);
    color: var(--ink-dark);
  }
  .logo-frame {
    position: absolute;
    left: 190px;
    top: 70px;
    width: 360px;
    height: 190px;
    border: 1.5px solid var(--brand-orange);
  }
  .wordmark {
    position: absolute;
    left: 0;
    right: 0;
    top: 130px;
    display: flex;
    justify-content: center;
    align-items: center;
    gap: 16px;
    padding-left: 20px;
  }
  .wordmark__square {
    width: 24px;
    height: 24px;
    background: var(--brand-orange);
  }
  .wordmark__name {
    font-family: "Libre Baskerville", Georgia, serif;
    font-weight: 400;
    font-size: 50px;
    color: var(--ink-dark);
    letter-spacing: 1px;
  }
  .tagline {
    position: absolute;
    left: 0;
    right: 0;
    top: 300px;
    text-align: center;
    font-family: "Poppins", Arial, sans-serif;
    font-weight: 400;
    font-size: 15px;
    letter-spacing: 2.4px;
    text-transform: uppercase;
    color: var(--ink-dark);
  }
  .tagline__accent { color: var(--brand-orange); }
</style>
</head>
<body>
<main class="canvas">
  <section class="card card--front" aria-label="Business card front">
    <div class="card__frame"></div>
    <div class="contact-block">
      <div class="person">
        <p class="person__name">Daniel Reyes</p>
        <p class="person__title">President</p>
      </div>
      <div class="divider"></div>
      <ul class="details">
        <li>555-204-7719</li>
        <li>daniel@quillmorrow.net</li>
        <li>www.quillmorrow.net</li>
      </ul>
    </div>
  </section>

  <section class="card card--back" aria-label="Business card back">
    <div class="logo-frame"></div>
    <div class="wordmark">
      <span class="wordmark__square"></span>
      <span class="wordmark__name">Quill Morrow</span>
    </div>
    <p class="tagline">Clearer thinking, <span class="tagline__accent">bolder results</span></p>
  </section>
</main>
</body>
</html>
```